I am looking for a modern, clean and neat design for a reflexology and well being business. The business name is Lumen Orto (this is an old Latin word for wellbeing). The colours I would like are purple, white and grey. I am open to suggestions for pictures such as healing or working hands, a pair of feet, images that represent my business that you may think of....... or maybe you think no images at all would be best? My tag line is: "Relax, Renew, Revive" or "Find you balance......... Relax, Renew, Revive" I can decide which I want so I would like to see what both would look like. I would like space on the back to write the client's appointment date and time (more than once)

```html
<!DOCTYPE html>
<html lang="en">
<head>
<meta charset="utf-8">
<title>Lumen Orto – Business Card</title>
<link href="https://fonts.googleapis.com/css2?family=Source+Sans+3:wght@300;400&display=swap" rel="stylesheet">
<style>
  :root {
    --backdrop: #ffb56b;
    --accent-purple: #7b3fa6;
    --slate: #5a5a5c;
    --paper-light: #f2f2f2;
    --paper-shade: #c3c3c5;
    --ink: #111111;
    --ink-soft: #555555;
    --rule: #777777;
  }
  * { margin: 0; padding: 0; box-sizing: border-box; }
  html, body {
    width: 1200px; height: 1200px; overflow: hidden;
    background: var(--backdrop);
    font-family: "Source Sans 3", sans-serif;
  }
  .canvas { position: relative; width: 1200px; height: 1200px; }
  .card {
    position: absolute; left: 166px; width: 869px; height: 496px; overflow: hidden;
  }
  .card--front { top: 58px; }
  .card--back { top: 628px; }
  .card__art { position: absolute; inset: 0; width: 100%; height: 100%; }

  .brand-dot {
    position: absolute; left: 110px; top: 44px; width: 100px; height: 100px;
    border-radius: 50%; background: var(--accent-purple);
  }
  .brand-name {
    position: absolute; left: 50px; top: 170px;
    font-size: 69px; font-weight: 400; color: var(--ink); letter-spacing: -0.5px;
    line-height: 1;
  }
  .tagline {
    position: absolute; left: 54px; top: 256px;
    font-size: 22px; font-weight: 300; line-height: 1.2; color: var(--ink-soft);
    letter-spacing: 0.3px;
  }
  .tagline__lead { color: var(--accent-purple); font-weight: 400; }
  .contact {
    position: absolute; top: 401px;
    font-size: 18px; font-weight: 300; line-height: 23px; color: var(--ink-soft);
    white-space: nowrap;
  }
  .contact::before {
    content: ""; display: block; width: 79px; height: 7px;
    background: var(--accent-purple); margin-bottom: 6px;
  }
  .contact--address { left: 44px; }
  .contact--phone { left: 258px; }
  .contact--web { left: 461px; }
  .contact-divider {
    position: absolute; top: 401px; width: 2px; height: 47px; background: var(--rule);
  }
  .contact-divider--one { left: 234px; }
  .contact-divider--two { left: 437px; }
</style>
</head>
<body>
<div class="canvas">

  <section class="card card--front">
    <svg class="card__art" viewBox="0 0 1086 620" preserveAspectRatio="none" aria-hidden="true">
      <defs>
        <linearGradient id="paperFront" x1="0" y1="1" x2="1" y2="0">
          <stop offset="0" stop-color="var(--paper-shade)"/>
          <stop offset="0.7" stop-color="var(--paper-light)"/>
        </linearGradient>
      </defs>
      <rect width="1086" height="620" fill="var(--slate)"/>
      <polygon points="545,0 643,0 1086,425 1086,515" fill="var(--accent-purple)"/>
      <polygon points="985,430 1040,445 881,620 833,620" fill="var(--accent-purple)"/>
      <polygon points="0,0 545,0 1003,440 833,620 0,620" fill="url(#paperFront)"/>
    </svg>
    <div class="brand-dot"></div>
    <h1 class="brand-name">Lumen Orto</h1>
    <p class="tagline"><span class="tagline__lead">Find your balance…</span> Relax, Renew, Revive</p>
    <p class="contact contact--address">14 Willow Lane,<br>Greenfield, GF3 7QA</p>
    <span class="contact-divider contact-divider--one"></span>
    <p class="contact contact--phone">ph.: 01632 960 418<br>mob.: 07700 900 572</p>
    <span class="contact-divider contact-divider--two"></span>
    <p class="contact contact--web">email: hello@lumenorto.example<br>site: www.lumenorto.example</p>
  </section>

  <section class="card card--back">
    <svg class="card__art" viewBox="0 0 1086 620" preserveAspectRatio="none" aria-hidden="true">
      <defs>
        <linearGradient id="paperBack" x1="0" y1="0.5" x2="1" y2="0.5">
          <stop offset="0" stop-color="#d6d6d8"/>
          <stop offset="0.6" stop-color="var(--paper-light)"/>
          <stop offset="1" stop-color="#ececec"/>
        </linearGradient>
      </defs>
      <rect width="1086" height="620" fill="var(--slate)"/>
      <polygon points="393,0 478,0 203,293 158,250" fill="var(--accent-purple)"/>
      <polygon points="0,105 543,620 440,620 0,200" fill="var(--accent-purple)"/>
      <polygon points="478,0 1086,0 1086,620 543,620 203,293" fill="url(#paperBack)"/>
      <g class="appointment-lines" stroke="var(--accent-purple)" stroke-width="3">
        <line x1="494" y1="103" x2="1017" y2="103"/>
        <line x1="494" y1="207" x2="1017" y2="207"/>
        <line x1="494" y1="310" x2="1017" y2="310"/>
      </g>
    </svg>
  </section>

</div>
</body>
</html>
```